Tembo & Lusani Advocates website

An interactive professional law firm website fully synchronized with social media pages.

Target Market(s)

Corporations and professionals

Industry/Entity Type

Professional Service

Number of Pages Required

5+ page

Font styles to use
Sans Serif

Colors

Designer to choose colors to be used in the design.

```html
<!DOCTYPE html>
<html lang="en">
<head>
<meta charset="utf-8">
<title>Tembo &amp; Lusani Advocates</title>
<link href="https://fonts.googleapis.com/css2?family=Mulish:wght@400;600;700;800&display=swap" rel="stylesheet">
<style>
:root{
  --maroon:#7b0c1c;
  --ink:#222;
  --text:#444;
  --grey:#efefef;
  --footer:#333;
  --white:#fff;
  --line:#ccc;
}
*{box-sizing:border-box;margin:0;padding:0}
html,body{width:1200px;height:2799px;overflow:hidden}
body{font-family:'Mulish',sans-serif;color:var(--text);background:var(--white);position:relative}
.band{position:absolute;left:0;width:1200px}
.section-title{font-weight:800;color:var(--maroon);font-size:40px;text-align:center;position:absolute;left:0;width:1200px}

/* header */
.site-header{top:0;height:127px;background:var(--white)}
.brand{position:absolute;left:133px;top:38px;display:flex;align-items:center;gap:12px}
.brand-square{width:26px;height:26px;background:var(--maroon)}
.brand-name{font-size:24px;font-weight:700;color:var(--maroon);white-space:nowrap}
.contact-bar{position:absolute;right:132px;top:30px;font-size:16px;color:var(--ink);display:flex;align-items:center;gap:8px}
.contact-bar svg{width:12px;height:12px}
.main-nav{position:absolute;right:132px;top:88px;display:flex;gap:28px;font-size:13px;color:#333}
.main-nav .active{color:var(--maroon)}

/* hero */
.hero{top:127px;height:487px;background:linear-gradient(180deg,#3a3530 0%,#1d1f24 55%,#2b2a2c 100%)}
.hero-arrow{position:absolute;top:230px;width:20px;height:24px}

/* about */
.about{top:614px;height:435px}
.about .section-title{top:72px}
.about-text{position:absolute;left:133px;width:934px;top:127px;text-align:center;font-size:16.5px;line-height:28px;color:#444}
.statement{position:absolute;top:235px;width:452px;height:120px;border:1px solid var(--line);text-align:center;padding-top:22px}
.statement h3{font-size:26px;font-weight:700;color:var(--ink);letter-spacing:.5px}
.statement p{font-size:11px;line-height:18px;color:#444;padding:8px 24px 0}

/* practice */
.practice{top:1049px;height:491px;background:var(--grey)}
.practice .section-title{top:64px}
.practice-card{position:absolute;top:141px;width:298px;height:268px;background:var(--maroon);color:var(--white);text-align:center;padding-top:28px}
.practice-card svg{width:78px;height:62px}
.practice-card h3{font-size:20px;font-weight:700;margin-top:12px;letter-spacing:.3px}
.practice-card p{font-size:11px;line-height:18px;padding:6px 22px 0;height:64px}
.read-more{display:inline-block;margin-top:10px;border:1px solid var(--white);font-size:11px;padding:9px 16px}

/* clients */
.clients{top:1540px;height:352px}
.clients .section-title{top:62px}
.client-tabs{position:absolute;top:130px;left:0;width:1200px;text-align:center;font-size:16px;color:#555}
.client-tabs .active{color:var(--maroon);text-decoration:underline;font-weight:600}
.client-tabs .sep{margin:0 12px}
.client-row{position:absolute;top:183px;left:180px;display:flex;gap:37px}
.client-tile{width:87px;height:87px;border:1px solid #e2e2e2;border-radius:8px;display:flex;flex-direction:column;align-items:center;justify-content:center;gap:5px;font-size:11px;font-weight:700;color:#333;text-align:center;line-height:1.2}
.client-tile i{display:block;width:14px;height:14px;border-radius:50%;background:var(--maroon)}

/* professionals */
.team{top:1892px;height:513px;background:var(--grey)}
.team .section-title{top:65px}
.member{position:absolute;top:157px;width:240px;text-align:center}
.member-photo{width:211px;height:211px;border-radius:50%;margin:0 auto;background:radial-gradient(circle at 50% 35%,#4e7f9a 0%,#26394a 55%,#14181d 100%)}
.member h4{margin-top:12px;font-size:15px;font-weight:800;color:var(--maroon)}
.member p{font-size:12.5px;color:#333;margin-top:4px;line-height:16px}
.team-arrow{position:absolute;top:251px;width:14px;height:22px}

/* contact */
.contact{top:2405px;height:290px}
.contact .section-title{top:74px}
.contact-lines{position:absolute;top:130px;left:0;width:1200px;text-align:center;font-size:17px;color:#222;line-height:29px}

/* footer */
.site-footer{top:2695px;height:104px;background:var(--footer);color:#ccc}
.footer-nav{position:absolute;left:133px;top:28px;font-size:11.5px}
.footer-nav .sep{margin:0 8px}
.copyright{position:absolute;left:133px;top:57px;font-size:11.5px}
.social{position:absolute;right:132px;top:36px;display:flex;gap:18px}
.social i{display:block;width:14px;height:14px;border-radius:50%;background:#ccc}
</style>
</head>
<body>

<header class="band site-header">
  <div class="brand">
    <div class="brand-square"></div>
    <div class="brand-name">Tembo &amp; Lusani Advocates</div>
  </div>
  <div class="contact-bar">
    <svg viewBox="0 0 12 12"><path d="M2.5 1l2 2.2-1 1.3c.7 1.5 1.6 2.4 3 3l1.3-1 2.2 2-1 1.8C5 10 2 7 .9 2z" fill="#222"/></svg>
    <span>Phone : 0414 550 218</span>
    <span style="margin:0 6px">|</span>
    <svg viewBox="0 0 12 12"><rect x="3" y=".5" width="6" height="11" rx="1" fill="none" stroke="#222" stroke-width="1.3"/><rect x="5" y="9" width="2" height="1" fill="#222"/></svg>
    <span>Mobile : +256 (0) 750 660 417</span>
  </div>
  <nav class="main-nav">
    <span class="active">Who We Are</span><span>How We Do It</span><span>Practice Areas</span><span>Clients</span><span>Team</span><span>Contact Us</span>
  </nav>
</header>

<section class="band hero" role="img" aria-label="Group photograph of the firm's advocates in business suits">
  <svg class="hero-arrow" style="left:52px" viewBox="0 0 20 24"><path d="M14 5 7 12l7 7" fill="none" stroke="#fff" stroke-width="3.5"/></svg>
  <svg class="hero-arrow" style="right:52px" viewBox="0 0 20 24"><path d="M6 5l7 7-7 7" fill="none" stroke="#fff" stroke-width="3.5"/></svg>
</section>

<section class="band about">
  <h2 class="section-title">Who We Are</h2>
  <p class="about-text">Tembo &amp; Lusani Advocates are a specialist commercial law firm in Uganda focusing on commercial litigation, construction law and arbitration. We have excelled in our niche areas for over two decades and we continue to grow and be the firm choice in those practice areas.</p>
  <div class="statement" style="left:133px">
    <h3>VISION</h3>
    <p>To be the firm of choice in our niche practice areas of commercial law.</p>
  </div>
  <div class="statement" style="left:615px">
    <h3>MISSION</h3>
    <p>To provide legal services focused on commercial litigation, construction law and arbitration with efficiency, integrity and client satisfaction.</p>
  </div>
</section>

<section class="band practice">
  <h2 class="section-title">Practice Areas</h2>
  <div class="practice-card" style="left:133px">
    <svg viewBox="0 0 78 62" fill="none" stroke="#fff" stroke-width="2.5"><path d="M10 46a29 29 0 0 1 58 0"/><path d="M31 18v-8h16v8M33 10v26M45 10v26"/><rect x="4" y="46" width="70" height="8" rx="3"/></svg>
    <h3>CONSTRUCTION LAW</h3>
    <p>Our Construction Law department is headed by our Senior Partner Daniel Tembo, who is highly qualified and experienced in Construction law...</p>
    <span class="read-more">Read More</span>
  </div>
  <div class="practice-card" style="left:451px">
    <svg viewBox="0 0 78 62" fill="none" stroke="#fff" stroke-width="2.5"><rect x="22" y="4" width="32" height="50"/><path d="M28 4V1h20v3M28 16h20M28 24h20M28 32h20M28 40h12"/><path d="M52 46l10-22 4 2-10 22-5 2z"/></svg>
    <h3>COMMERCIAL LITIGATION</h3>
    <p>We have a reputation for producing excellent results for our litigation clients. Since 1996, the firm has an excellent track record...</p>
    <span class="read-more">Read More</span>
  </div>
  <div class="practice-card" style="left:769px">
    <svg viewBox="0 0 78 62" fill="none" stroke="#fff" stroke-width="2.5"><rect x="24" y="2" width="30" height="18" rx="2"/><path d="M30 8h18M30 14h12"/><circle cx="22" cy="30" r="5"/><circle cx="56" cy="30" r="5"/><path d="M12 50v-8a10 10 0 0 1 20 0M46 42a10 10 0 0 1 20 0v8M8 50h62M18 50v10M60 50v10"/></svg>
    <h3>ARBITRATION</h3>
    <p>We advise clients on both domestic and international arbitration proceedings and other forms of intermediate and alternative...</p>
    <span class="read-more">Read More</span>
  </div>
</section>

<section class="band clients">
  <h2 class="section-title">Our Clients</h2>
  <div class="client-tabs"><span class="active">Commercial Litigation and Transactions</span><span class="sep">|</span><span>Construction &amp; Arbitration</span><span class="sep">|</span><span>Corporate Advisory</span></div>
  <div class="client-row">
    <div class="client-tile"><i></i>Swiftline</div>
    <div class="client-tile"><i></i>Savanna<br>Foods</div>
    <div class="client-tile"><i></i>Redstone<br>Bank</div>
    <div class="client-tile"><i></i>Crestmark<br>Insurance</div>
    <div class="client-tile"><i></i>Packwell</div>
    <div class="client-tile"><i></i>Motorhub</div>
    <div class="client-tile"><i></i>Greenway<br>Traders</div>
  </div>
</section>

<section class="band team">
  <h2 class="section-title">Our Professionals</h2>
  <svg class="team-arrow" style="left:55px" viewBox="0 0 14 22"><path d="M11 3 3 11l8 8" fill="none" stroke="#555" stroke-width="2"/></svg>
  <div class="member" style="left:119px"><div class="member-photo" role="img" aria-label="Portrait photograph of Peter M. Tembo"></div><h4>PETER M. TEMBO</h4><p>Managing Partner</p></div>
  <div class="member" style="left:360px"><div class="member-photo" role="img" aria-label="Portrait photograph of Daniel R. Tembo"></div><h4>DANIEL R. TEMBO</h4><p>Senior Partner</p></div>
  <div class="member" style="left:600px"><div class="member-photo" role="img" aria-label="Portrait photograph of Simon Okello"></div><h4>SIMON OKELLO</h4><p>Partner (Head of Litigation )</p></div>
  <div class="member" style="left:841px"><div class="member-photo" role="img" aria-label="Portrait photograph of Nathan Kirabo"></div><h4>NATHAN KIRABO</h4><p>Partner (Head of Business<br>Developments)</p></div>
  <svg class="team-arrow" style="right:55px" viewBox="0 0 14 22"><path d="M3 3l8 8-8 8" fill="none" stroke="#555" stroke-width="2"/></svg>
</section>

<section class="band contact">
  <h2 class="section-title">Contact Us</h2>
  <div class="contact-lines">
    <div style="font-size:16px">Head Office Address &amp; Contacts</div>
    <div>Plot 14, Jacaranda Road 3rd Floor, Mvule House P. O Box 4127. Kampala, Uganda.</div>
    <div>Phone : 0414 550 218 &nbsp; | &nbsp; Mobile : +256 (0) 750 660 417 &nbsp; | &nbsp; Email : advocates@tembolusani.com</div>
  </div>
</section>

<footer class="band site-footer">
  <div class="footer-nav">Who We Are<span class="sep">|</span>How We Do It<span class="sep">|</span>Practice Areas<span class="sep">|</span>Clients<span class="sep">|</span>Team<span class="sep">|</span>Contact Us</div>
  <div class="copyright">Copyright &copy; 2018 Tembo and Lusani Advocates. &nbsp; All rights reserved.</div>
  <div class="social"><i></i><i></i><i></i></div>
</footer>

</body>
</html>
```